Home Builder and Trade Supplier needs a Ad/leaflet/mail drop off leaflet design

HavenCrest is a business that builds homes, renovations, property maintenance and anything else construction related to residential homes. See photos I have attached that have a description of the business.

I'm after a double sided flyer for mail box drop offs. The market audience is up market expensive homes and offices. I have attached some examples of what i think would look good - I would like to see an example like or similar to that but by all means the designs you submit don't have to be a copy or similar. If you have something completely different in mind that you think would suit, please submit or even a rough draft if youre not sure I'll like it and you don't want to risk wasting time.

Please include the text and information in your designs that I have included in my examples.

Submissions before the 10 days are welcome and encouraged :)

Any questions, please feel free to ask on here or through email on: joram.k@mailvista.net

Pamphlet Size: 210 x 142mm (a quarter of an A4)
Double Sided Colour

Property Maintenance

Requirements
Must have
• Contact Us: 0412 958 601
www.havencresthomes.com.au
Double sided
Colour
Size: quater of an A4

```html
<!DOCTYPE html>
<html lang="en">
<head>
<meta charset="utf-8">
<title>HavenCrest – Property Maintenance Flyer</title>
<link href="https://fonts.googleapis.com/css2?family=Questrial&display=swap" rel="stylesheet">
<style>
  :root {
    --paper-centre: #ffffff;
    --paper-edge: #ececec;
    --brand-orange: #e95a27;
    --mark-grey: #c4c5c7;
    --text-grey: #8e8f92;
    --steel-light: #f0f0f0;
    --steel-mid: #b4b4b6;
    --steel-dark: #8f8f92;
    --handle-yellow: #f4c52c;
    --handle-amber: #e6b01e;
    --handle-dark: #3b3b3d;
  }
  html, body {
    margin: 0;
    padding: 0;
    width: 852px;
    height: 1200px;
    overflow: hidden;
    background: #ffffff;
  }
  .flyer {
    position: relative;
    width: 852px;
    height: 1200px;
    overflow: hidden;
    background: radial-gradient(ellipse at 50% 50%, var(--paper-centre) 0%, var(--paper-centre) 40%, var(--paper-edge) 100%);
  }
  .tool-frame {
    position: absolute;
    inset: 0;
    width: 852px;
    height: 1200px;
  }
  .brand {
    position: absolute;
    left: 219px;
    top: 528px;
    display: flex;
    align-items: center;
    gap: 18px;
  }
  .brand__square {
    width: 132px;
    height: 138px;
    background: var(--mark-grey);
  }
  .brand__name {
    margin: 0;
    font-family: "Questrial", sans-serif;
    font-weight: 400;
    font-size: 76px;
    line-height: 72px;
    color: var(--brand-orange);
    letter-spacing: 1px;
    text-transform: uppercase;
  }
  .brand__name span { display: block; }
  .contact {
    position: absolute;
    left: 0;
    right: 0;
    top: 700px;
    margin: 0;
    text-align: center;
    font-family: "Questrial", sans-serif;
    font-size: 19px;
    line-height: 28px;
    color: var(--text-grey);
    letter-spacing: 0.5px;
  }
  .contact span { display: block; }
</style>
</head>
<body>
  <main class="flyer">
    <svg class="tool-frame" viewBox="0 0 852 1200" xmlns="http://www.w3.org/2000/svg">
      <defs>
        <linearGradient id="tool-yellow" x1="0" y1="0" x2="1" y2="0">
          <stop offset="0" stop-color="var(--steel-light)"/>
          <stop offset="0.45" stop-color="var(--steel-mid)"/>
          <stop offset="0.6" stop-color="var(--handle-yellow)"/>
          <stop offset="1" stop-color="var(--handle-amber)"/>
        </linearGradient>
        <linearGradient id="tool-dark" x1="0" y1="0" x2="1" y2="0">
          <stop offset="0" stop-color="var(--steel-light)"/>
          <stop offset="0.45" stop-color="var(--steel-mid)"/>
          <stop offset="0.62" stop-color="#4a4a4c"/>
          <stop offset="1" stop-color="var(--handle-dark)"/>
        </linearGradient>
        <linearGradient id="tool-steel" x1="0" y1="0" x2="1" y2="0">
          <stop offset="0" stop-color="var(--steel-light)"/>
          <stop offset="1" stop-color="var(--steel-dark)"/>
        </linearGradient>
      </defs>

      <!-- top edge -->
      <g role="img" aria-label="Illustration of a vernier caliper"><rect x="-165" y="-35" width="330" height="70" rx="10" fill="url(#tool-steel)" transform="translate(135 118) rotate(45)"/></g>
      <g role="img" aria-label="Illustration of end-cutting pliers with yellow handles"><rect x="-115" y="-50" width="230" height="100" rx="18" fill="url(#tool-yellow)" transform="translate(326 108) rotate(-90)"/></g>
      <g role="img" aria-label="Illustration of a wood chisel"><rect x="-120" y="-18" width="240" height="36" rx="8" fill="url(#tool-yellow)" transform="translate(468 117) rotate(-90)"/></g>
      <g role="img" aria-label="Illustration of a flat screwdriver"><rect x="-120" y="-11" width="240" height="22" rx="8" fill="url(#tool-yellow)" transform="translate(560 117) rotate(-90)"/></g>
      <g role="img" aria-label="Illustration of water pump pliers"><rect x="-150" y="-45" width="300" height="90" rx="16" fill="url(#tool-dark)" transform="translate(730 100) rotate(-41)"/></g>

      <!-- right edge -->
      <g role="img" aria-label="Illustration of a hand saw blade"><rect x="-135" y="-30" width="270" height="60" rx="6" fill="url(#tool-steel)" transform="translate(750 255) rotate(-40)"/></g>
      <g role="img" aria-label="Illustration of long-nose pliers"><rect x="-125" y="-35" width="250" height="70" rx="16" fill="url(#tool-yellow)" transform="translate(756 405) rotate(-38)"/></g>
      <g role="img" aria-label="Illustration of a cordless drill"><rect x="-85" y="-35" width="170" height="70" rx="16" fill="url(#tool-yellow)" transform="translate(782 565) rotate(-33)"/></g>
      <g role="img" aria-label="Illustration of a tape measure"><rect x="-95" y="-68" width="190" height="136" rx="30" fill="url(#tool-yellow)" transform="translate(785 805) rotate(90)"/></g>
      <g role="img" aria-label="Illustration of scissors"><rect x="-125" y="-28" width="250" height="56" rx="14" fill="url(#tool-dark)" transform="translate(757 955) rotate(42)"/></g>
      <g role="img" aria-label="Illustration of an adjustable wrench"><rect x="-140" y="-40" width="280" height="80" rx="18" fill="url(#tool-yellow)" transform="translate(758 1098) rotate(48)"/></g>

      <!-- left edge -->
      <g role="img" aria-label="Illustration of a hacksaw"><rect x="-150" y="-35" width="300" height="70" rx="12" fill="url(#tool-dark)" transform="translate(86 266) rotate(57)"/></g>
      <g role="img" aria-label="Illustration of a saw blade"><rect x="-115" y="-20" width="230" height="40" rx="6" fill="url(#tool-steel)" transform="translate(100 430) rotate(211)"/></g>
      <g role="img" aria-label="Illustration of a G-clamp"><rect x="-100" y="-66" width="200" height="132" rx="20" fill="url(#tool-yellow)" transform="translate(68 574) rotate(-75)"/></g>
      <g role="img" aria-label="Illustration of a cross-peen hammer"><rect x="-105" y="-30" width="210" height="60" rx="12" fill="url(#tool-yellow)" transform="translate(75 790) rotate(135)"/></g>
      <g role="img" aria-label="Illustration of an open-end spanner"><rect x="-90" y="-27" width="180" height="54" rx="20" fill="url(#tool-steel)" transform="translate(55 935) rotate(126)"/></g>
      <g role="img" aria-label="Illustration of a claw hammer"><rect x="-130" y="-30" width="260" height="60" rx="14" fill="url(#tool-yellow)" transform="translate(100 1100) rotate(135)"/></g>

      <!-- bottom edge -->
      <g role="img" aria-label="Illustration of a broad chisel"><rect x="-100" y="-42" width="200" height="84" rx="12" fill="url(#tool-dark)" transform="translate(282 1104) rotate(90)"/></g>
      <g role="img" aria-label="Illustration of a metal file"><rect x="-100" y="-12" width="200" height="24" rx="4" fill="url(#tool-dark)" transform="translate(408 1100) rotate(90)"/></g>
      <g role="img" aria-label="Illustration of combination pliers"><rect x="-105" y="-60" width="210" height="120" rx="22" fill="url(#tool-yellow)" transform="translate(555 1098) rotate(90)"/></g>
    </svg>

    <div class="brand">
      <span class="brand__square" aria-hidden="true"></span>
      <h1 class="brand__name"><span>Haven</span><span>Crest</span></h1>
    </div>

    <p class="contact">
      <span>Contact Us: 0412 958 601</span>
      <span>www.havencresthomes.com.au</span>
    </p>
  </main>
</body>
</html>
```